My name is Tomas Verenda, and I have done business with your company several times. I need a business card to represent my business, I own a company by the name of BELOMI Suntan Lotion & Sunscreen.
My requirements are as follow: My company logo in the brightest gold possible, on a black, grainy (sandy) background, with shading around the each element. With the company name in gold, a stylized coconut trees, and some type of wave graphic in gold. "A product of the USA, Staten Island, NY"
"For comments, suggestion, or ordering please contact us at:
belomi42@nexamail.test"

"BELOMI™ Tanning Lotion & Sunscreen―Crafted with Care"

Belomi Tanning Lotion & Sunscreen is the most extraordinary and innovative sun tanning product to emerge in several generations. The constituents of this product are formidable substances that protect the skin against the aftermath of sun exposure−before you exposed yourself to the sun’s rays. The Aloe Vera in this product, along with other oils and cream, are specifically manufactured to lessen the symptoms of extended exposure to the sun. Belomi is designed to provide a Broad Spectrum Protection (50) that assist in the reduction of (UVA) and (UVB) radiation to create a magnificent sun-absorbing, long-lasting, deep dark bronzing experience.
Thank you,
Tomas Verenda
tomastverenda@postline.test

Target Market(s)

Sunscreen

Industry/Entity Type

Business

Contact Information for Business Card

BELOMI™ Tanning Lotion and Sunscreen
Crafted with Care

Belomi Tanning Lotion is the most extraordinary and innovative sun tanning product to emerge in several generations. The constituents of this product are formidable substances that protect the skin against the aftermath of sun exposure−before you exposed yourself to the sun’s rays. The Aloe Vera, in this product, along with other oils and cream, are specifically manufactured to lessen the symptoms of extended exposure to the sun. Belomi protects your skin from dehydration and treat your skin with the products we apply to ourselves after a sunburn−before the sun tanning process begins. Belomi is designed to provide a Broad Spectrum Protection (50) that assist in the reduction of (UVA) and (UVB) radiation to create a magnificent sun-absorbing, long-lasting, deep dark bronzing experience.

Colors
fece3e
acd136

Requirements
Must have
• Black Card Stock with grainy surface, Gold Logo, stylized Coconut Palm Tree, Company Name, email address, and NYC location.
• Modern Layout with Modern fonts and graphics

```html
<!DOCTYPE html>
<html lang="en">
<head>
<meta charset="utf-8">
<title>BELOMI Suntan Lotion – Business Card</title>
<link href="https://fonts.googleapis.com/css2?family=Cabin:wght@400;500;600;700&display=swap" rel="stylesheet">
<style>
  :root {
    --page: #ececec;
    --card: #474c4c;
    --card-shade: #3f4545;
    --band: #3b4a4d;
    --gold: #c9a66b;
    --yellow: #fece3e;
    --lime: #acd136;
    --frond-dark: rgba(47,107,50,.85);
    --frond-light: #5fae4a;
    --frond-fade: rgba(47,107,50,0);
  }
  * { box-sizing: border-box; margin: 0; padding: 0; }
  html, body {
    width: 1200px; height: 1000px; overflow: hidden;
    background: var(--page);
    font-family: "Cabin", sans-serif;
  }
  .sheet {
    position: relative; width: 1200px; height: 1000px;
    display: flex; align-items: center; justify-content: center; gap: 40px;
  }
  .card {
    position: relative; width: 520px; height: 297px; overflow: hidden;
    background: linear-gradient(160deg, var(--card) 0%, var(--card-shade) 100%);
    box-shadow: 0 14px 30px rgba(0,0,0,.18);
  }
  .brand { display: flex; align-items: center; gap: 8px; }
  .brand-name {
    font-weight: 600; font-size: 30px; letter-spacing: 2px; color: var(--gold);
    line-height: 1;
  }
  .brand-dot { width: 30px; height: 30px; border-radius: 50%; background: var(--gold); }
  .brand-tag {
    font-size: 10px; letter-spacing: 2px; color: var(--gold);
    text-transform: uppercase; margin-top: 3px; padding-left: 6px;
  }
  .frond {
    position: absolute; z-index: 0;
    background: radial-gradient(closest-side, var(--frond-light) 0%, var(--frond-dark) 55%, var(--frond-fade) 100%);
  }
  /* front */
  .front .brand-block { position: absolute; left: 34px; top: 30px; z-index: 1; }
  .front .person { position: absolute; left: 34px; top: 104px; z-index: 1; }
  .person-name {
    font-size: 24px; font-weight: 500; color: var(--yellow);
    text-transform: uppercase; letter-spacing: .5px;
  }
  .person-role { font-size: 15px; color: var(--yellow); text-transform: uppercase; margin-top: 2px; }
  .contact-list { list-style: none; margin-top: 12px; }
  .contact-list li {
    display: flex; align-items: center; gap: 9px;
    font-size: 15px; color: var(--lime); margin-bottom: 12px;
  }
  .contact-icon { width: 18px; height: 18px; flex: none; }
  .front .frond { left: 300px; top: 90px; width: 260px; height: 240px; }
  /* back */
  .back-note {
    position: absolute; left: 40px; right: 30px; top: 30px; z-index: 1;
    text-align: center; font-size: 14px; font-weight: 600; line-height: 1.35;
    color: var(--yellow);
  }
  .back-band {
    position: absolute; left: 0; right: 0; top: 124px; height: 104px;
    background: var(--band);
    display: flex; align-items: center; gap: 34px; padding-left: 26px;
  }
  .back-band > * { position: relative; z-index: 1; }
  .back-band .brand-name { font-size: 20px; }
  .back-band .brand-dot { width: 22px; height: 22px; }
  .back-band .brand-tag { font-size: 8px; }
  .address { font-size: 14px; color: var(--lime); line-height: 1.3; }
  .website { font-size: 17px; font-weight: 700; color: var(--lime); margin-top: 8px; }
  .back .frond { left: 350px; top: 200px; width: 190px; height: 120px; }
</style>
</head>
<body>
<main class="sheet">
  <section class="card front" aria-label="Business card front">
    <div class="frond" role="img" aria-label="Green palm frond"></div>
    <div class="brand-block">
      <div class="brand"><span class="brand-name">BELOMI</span><span class="brand-dot"></span></div>
      <div class="brand-tag">Suntan Lotion</div>
    </div>
    <div class="person">
      <p class="person-name">Tomas Verenda</p>
      <p class="person-role">Owner</p>
      <ul class="contact-list">
        <li>
          <svg class="contact-icon" viewBox="0 0 18 18"><circle cx="9" cy="9" r="9" fill="#fece3e"/><path d="M6 5h2l1 2.5-1.2.8a6 6 0 0 0 2 2l.8-1.2L13 10v2a1 1 0 0 1-1 1A7 7 0 0 1 5 6a1 1 0 0 1 1-1z" fill="#474c4c"/></svg>
          000-000-0000
        </li>
        <li>
          <svg class="contact-icon" viewBox="0 0 18 18"><circle cx="9" cy="9" r="9" fill="#fece3e"/><rect x="4.5" y="6" width="9" height="6.5" rx="1" fill="#474c4c"/><path d="M4.8 6.4 9 9.6l4.2-3.2" stroke="#fece3e" stroke-width="1" fill="none"/></svg>
          tomastverenda@postline.test
        </li>
      </ul>
    </div>
  </section>

  <section class="card back" aria-label="Business card back">
    <p class="back-note">
      “A product of the USA, Staten Island, NY”<br>
      “For comments, suggestion, or ordering please contact us at:<br>
      belomi42@nexamail.test”
    </p>
    <div class="back-band">
      <div class="brand-block">
        <div class="brand"><span class="brand-name">BELOMI</span><span class="brand-dot"></span></div>
        <div class="brand-tag">Suntan Lotion</div>
      </div>
      <div>
        <p class="address">345 Lorem ipsum, main st.<br>Downtown, TX</p>
        <p class="website">www.yourwebsite.com</p>
      </div>
    </div>
    <div class="frond" role="img" aria-label="Green palm frond"></div>
  </section>
</main>
</body>
</html>
```